A new website for Electrical Contractor Business

We are looking for a unique and new WordPress website design which would include 5 Pages - Home Page, Meet the Team, Our Services, Our Projects and Contact Us page.

The global theme for the website needs to be professional but simple to navigate as we cater for both business and home owner customers.

Our core business service is targeted around lighting from single room decorative to large office so the theme should incorporate this in some way.

The home page should include;
Our business logo, Contact number, Email address, small Image rotation box - Highlighting pervious projectsText box - With welcome message, chirpnet feed news reel/Customer feed back box.

I would also like to see a 2 boxes for the separate customer types we services. Business and Home Owner. each box will have a small image with a small text description with a link to the area of the services page relevant to that customer type.

Meet the team page -This will be introducing potential customers to the team so I would like it to include for each team member. Something like a small image and text area which will introduce an outline of the team members skills and abilities.

Our Services page This page will be outlining the different services on offer to the both customer types business and homeowner. Each service should have an image with text description of the service would good here.

Our projects page-Will include images of pervious projects and work we have completed along with a text area for the project description/ outliner.

Contact Us page - Should include a contact form which should include an option for the customer to quest us to call them back, also a selection box for them to inform us our how they found our details would be good.

Colour - The theme colours can be taken from the logo or feel free to impress with your own imagination.

Remember we are looking for a website that will interest our customers enough to except our services or be drawn further into the website.. So call to action links to other areas of the site/ contact page are welcome

Target Market(s)

Business - Office, warehousing and Large Store - lighting and Power
Home owner lighting and power

Coding

Coded - Design and coding required

Number of Pages Required

5+ page

Font styles to use
Serif
Sans Serif

Colors

Designer to choose colors to be used in the design.

Requirements
Must have
• Logo integrated into the website design - i.e. website colours which allow the logo to blend into the design.
Nice to have
• Custom but professional theme catering to business customers, but also show that we do provide services to home owners too.
Should not have
• Sorry am not interested in one oversized block image on rotation covering half the home page.. Images will be needed but not a single block over sized frame with not text, shape. Please use your imagination when considering this design

```html
<!DOCTYPE html>
<html lang="en">
<head>
<meta charset="utf-8">
<title>Lumenwell Electric – Smart Lighting</title>
<link rel="stylesheet" href="https://fonts.googleapis.com/css2?family=Montserrat:wght@400;500;600;700;800&family=Open+Sans:ital,wght@0,400;0,600;1,400&display=swap">
<style>
:root{
  --navy:#1d2f66;
  --navy-deep:#16254f;
  --orange:#f26522;
  --orange-soft:#f58a4b;
  --ink:#2b2b2b;
  --muted:#7a7a7a;
  --line:#e6e6e6;
  --white:#ffffff;
}
*{box-sizing:border-box;margin:0;padding:0}
html,body{width:1200px;height:3830px;overflow:hidden;background:var(--white)}
body{position:relative;font-family:"Open Sans",Arial,sans-serif;color:var(--ink)}
.block{position:absolute;left:0;width:1200px}
.btn{display:inline-block;background:var(--orange);color:var(--white);font:700 11px "Montserrat",sans-serif;letter-spacing:1px;text-transform:uppercase;padding:13px 26px;text-decoration:none}
.btn-ghost{background:transparent;border:1px solid var(--white)}
.section-title{font:700 24px "Montserrat",sans-serif;color:var(--navy);text-transform:uppercase;text-align:center;letter-spacing:.5px}
.section-title span{color:var(--orange)}

/* top bar */
.topbar{top:0;height:41px;background:var(--navy);display:flex;align-items:center;padding:0 120px;font-size:12px;color:var(--white)}
.topbar .phone{color:var(--orange);font-weight:600;margin-right:28px;display:flex;align-items:center;gap:8px}
.topbar .mail{display:flex;align-items:center;gap:8px}
.topbar .socials{margin-left:auto;display:flex;gap:8px}
.social{width:16px;height:16px;border:1.5px solid var(--white);border-radius:3px}

/* nav */
.header{top:41px;height:92px;display:flex;align-items:center;padding:0 120px}
.brand{display:flex;align-items:center;gap:12px;font:700 20px "Montserrat",sans-serif;color:var(--navy);letter-spacing:.5px;text-transform:uppercase}
.brand .dot{width:40px;height:40px;border-radius:50%;background:var(--orange)}
.nav{margin-left:auto;display:flex;gap:44px;font:500 13px "Montserrat",sans-serif;color:var(--navy)}
.nav .active{color:var(--orange)}

/* hero */
.hero{top:133px;height:545px}
.hero-photo{position:absolute;inset:0;background:radial-gradient(ellipse at 50% 35%,#6a5ac8 0%,#3a3a88 40%,#1e2150 100%)}
.hero-shape{position:absolute;left:0;bottom:0;width:1200px;height:200px}
.hero-copy{position:absolute;top:190px;width:100%;text-align:center;color:var(--white)}
.hero-copy h1{font:700 39px/1.3 "Montserrat",sans-serif}
.hero-copy .btn{margin-top:38px}
.arrow{position:absolute;top:215px;width:14px;height:14px;border-top:2px solid var(--white);border-left:2px solid var(--white)}
.arrow.prev{left:58px;transform:rotate(-45deg)}
.arrow.next{right:58px;transform:rotate(135deg)}
.dots{display:flex;gap:8px;justify-content:center}
.dots i{width:11px;height:11px;border-radius:50%;border:1.5px solid #c9c9d9;display:block}
.dots i.on{border-color:var(--orange)}
.hero .dots{position:absolute;top:456px;width:100%}

/* about */
.about{top:780px;height:360px;padding:0 120px}
.about-copy{width:470px;padding-top:16px}
.about-copy h2{font:700 24px "Montserrat",sans-serif;color:var(--navy);text-transform:uppercase}
.about-copy h2 span{color:var(--orange)}
.about-copy p{margin-top:16px;font-size:13px;line-height:22px;color:var(--muted)}
.about-copy .btn{margin-top:34px}
.about-photo{position:absolute;left:656px;top:-26px;width:332px;height:368px}

/* customer types */
.types{top:1174px;height:400px}
.type{position:absolute;top:0;width:600px;height:400px;color:var(--white);text-align:center;padding-top:126px}
.type.home{left:0;background:linear-gradient(160deg,#3a5aa0,#1d3a78);clip-path:polygon(0 0,100% 14%,100% 100%,0 84%)}
.type.office{left:600px;background:linear-gradient(200deg,#f7a16a,#ee6b2d);clip-path:polygon(0 6%,100% 0,100% 96%,0 90%)}
.type h3{font:700 25px "Montserrat",sans-serif;letter-spacing:1px;text-transform:uppercase}
.type p{width:340px;margin:8px auto 0;font-size:13px;line-height:22px}
.type .btn{margin-top:22px;padding:10px 22px}

/* projects */
.projects{top:1602px;height:680px}
.gallery{position:absolute;top:70px;left:120px;width:960px;height:485px}
.tile{position:absolute}
.projects .btn{position:absolute;top:598px;left:537px}

/* testimonials */
.reviews{top:2310px;height:450px}
.review{position:absolute;top:64px;height:325px;background:var(--white);box-shadow:0 4px 18px rgba(0,0,0,.09);overflow:hidden;text-align:center}
.review p{position:relative;font-size:13px;line-height:22px;color:var(--muted);font-style:italic}
.review .wave{position:absolute;left:0;bottom:0}
.review .who{position:absolute;bottom:22px;width:100%;font:700 12px "Montserrat",sans-serif;color:var(--white)}
.review .avatar{position:absolute;left:50%;margin-left:-26px;bottom:48px;width:52px;height:52px;border-radius:50%;background:linear-gradient(#c7b29a,#7a6a5a);border:3px solid var(--white)}
.review .mark{width:20px;height:20px;border-radius:50%;background:#29a9e0;margin:34px auto 14px}
.review .quote{font:800 26px "Montserrat",sans-serif;color:var(--navy);margin:22px auto 4px}
.reviews .dots{position:absolute;top:414px}

/* team */
.team{top:2810px;height:480px}
.member{position:absolute;top:67px;width:296px;height:378px;background:var(--navy)}
.member .photo{height:156px}
.member .num{position:absolute;right:0;top:120px;width:52px;height:40px;background:var(--navy);border-radius:20px 0 0 0;color:var(--white);font:600 16px "Montserrat",sans-serif;text-align:center;line-height:44px}
.member h4{margin:30px 32px 0;font:700 17px "Montserrat",sans-serif;color:var(--orange);letter-spacing:1.5px;text-transform:uppercase}
.member .role{margin:2px 32px 0;font:600 9px "Montserrat",sans-serif;color:var(--white);letter-spacing:1px;text-transform:uppercase}
.member p{margin:18px 32px 0;font-size:12.5px;line-height:22px;color:#c9d1ea}
.member .more{margin:26px 32px 0;font:600 11px "Montserrat",sans-serif;color:var(--orange)}
.team .arrow{top:222px;border-color:var(--navy)}

/* footer */
.footer{top:3332px;height:498px}
.footer-bg{position:absolute;inset:0}
.footer-cols{position:absolute;top:176px;left:120px;display:flex}
.col{width:248px;color:var(--white);font-size:11px;line-height:20px}
.col h5{font:600 13px "Montserrat",sans-serif;margin-bottom:14px}
.col .current{color:var(--orange)}
.col .call{font:600 20px "Montserrat",sans-serif}
.col .call span,.col .orange{color:var(--orange)}
.col .socials{display:flex;gap:10px}
.copyright{position:absolute;bottom:0;width:100%;height:54px;border-top:1px solid rgba(255,255,255,.15);text-align:center;line-height:54px;font-size:11px;color:#aab4d4}
</style>
</head>
<body>

<div class="block topbar">
  <div class="phone">
    <svg width="12" height="12" viewBox="0 0 24 24"><path fill="#fff" d="M6.6 10.8a15 15 0 0 0 6.6 6.6l2.2-2.2a1 1 0 0 1 1-.25 11.4 11.4 0 0 0 3.6.57 1 1 0 0 1 1 1V20a1 1 0 0 1-1 1A17 17 0 0 1 3 4a1 1 0 0 1 1-1h3.5a1 1 0 0 1 1 1c0 1.25.2 2.45.57 3.57a1 1 0 0 1-.25 1z"/></svg>
    1-800-555-0142
  </div>
  <div class="mail">
    <svg width="13" height="10" viewBox="0 0 26 20"><rect x="1" y="1" width="24" height="18" fill="none" stroke="#fff" stroke-width="2"/><path d="M1 1l12 10 12-10" fill="none" stroke="#fff" stroke-width="2"/></svg>
    hello@lumenwell.example
  </div>
  <div class="socials"><span class="social"></span><span class="social"></span><span class="social"></span><span class="social"></span></div>
</div>

<header class="block header">
  <div class="brand"><span class="dot"></span>Lumenwell</div>
  <nav class="nav"><span class="active">Home</span><span>About</span><span>Services</span><span>Team</span><span>Project</span><span>Contact</span></nav>
</header>

<section class="block hero">
  <div class="hero-photo" role="img" aria-label="Modern open-plan living room lit with blue and violet accent lighting"></div>
  <svg class="hero-shape" viewBox="0 0 1200 200" preserveAspectRatio="none">
    <path d="M0 60 Q600 250 1200 60 L1200 200 L0 200Z" fill="#fff"/>
    <path d="M0 60 Q600 250 1200 60" fill="none" stroke="#f26522" stroke-width="7"/>
  </svg>
  <span class="arrow prev"></span><span class="arrow next"></span>
  <div class="hero-copy">
    <h1>Smart lighting, smart ideas<br>A Better Way Of Lighting</h1>
    <a class="btn">Know More</a>
  </div>
  <div class="dots"><i class="on"></i><i></i><i></i><i></i></div>
</section>

<section class="block about">
  <div class="about-copy">
    <h2>About <span>Lumenwell</span></h2>
    <p>Lorem ipsum dolor sit amet, consectetur adipiscing elit, sed do eiusmod tempor incididunt ut labore et dolore magna aliqua. Ut enim ad minim veniam, quis nostrud exercitation ullamco laboris nisi ut aliquip ex ea commodo consequat. Duis aute irure dolor in reprehenderit in voluptate velit esse cillum dolore eu fugiat nulla pariatur. Excepteur sint occaecat cupidatat non proident, sunt in culpa qui officia deserunt mollit anim id est laborum.</p>
    <a class="btn">Know More</a>
  </div>
  <svg class="about-photo" viewBox="0 0 332 368">
    <path d="M166 8 A160 160 0 0 1 326 168" fill="none" stroke="#f26522" stroke-width="14"/>
    <path d="M326 168 A160 160 0 1 1 166 8" fill="none" stroke="#1d2f66" stroke-width="14"/>
    <circle cx="166" cy="168" r="146" fill="#b8742e" role="img" aria-label="Staircase with warm under-step lighting"/>
    <circle cx="166" cy="168" r="146" fill="url(#warm)"/>
    <defs><radialGradient id="warm" cx=".45" cy=".4" r=".7"><stop offset="0" stop-color="#f0b060"/><stop offset="1" stop-color="#4a2a12"/></radialGradient></defs>
  </svg>
</section>

<section class="block types">
  <div class="type home" role="img" aria-label="Living room photo under a navy tint">
    <h3>Single Room</h3>
    <p>Lorem Ipsum is simply dummy text of the printing andtypesetting industry. Lorem Ipsum has industry's standard.</p>
    <a class="btn btn-ghost">Learn More</a>
  </div>
  <div class="type office" role="img" aria-label="Large office meeting room photo under an orange tint">
    <h3>Large Office</h3>
    <p>Lorem Ipsum is simply dummy text of the printing andtypesetting industry. Lorem Ipsum has industry's standard.</p>
    <a class="btn btn-ghost">Learn More</a>
  </div>
</section>

<section class="block projects">
  <h2 class="section-title">Our <span>Projects</span></h2>
  <div class="gallery">
    <div class="tile" style="left:0;top:0;width:462px;height:238px;background:linear-gradient(135deg,#c9b08a,#5e4a36)" role="img" aria-label="Home office with lit shelving"></div>
    <div class="tile" style="left:470px;top:0;width:240px;height:238px;background:linear-gradient(160deg,#c8a84a,#3c4a2a)" role="img" aria-label="Kitchen with round ceiling light"></div>
    <div class="tile" style="left:718px;top:0;width:242px;height:238px;background:linear-gradient(150deg,#e6e0d8,#9a8a7a)" role="img" aria-label="Bright open-plan office"></div>
    <div class="tile" style="left:0;top:245px;width:240px;height:240px;background:linear-gradient(160deg,#a0a4a8,#2a2a2a)" role="img" aria-label="Loft room with downlights"></div>
    <div class="tile" style="left:248px;top:245px;width:240px;height:240px;background:linear-gradient(160deg,#d8c0a0,#4a3424)" role="img" aria-label="Lounge with chandelier"></div>
    <div class="tile" style="left:496px;top:245px;width:464px;height:240px;background:linear-gradient(160deg,#8a5a38,#2a1a12)" role="img" aria-label="Dining room with pendant lamps"></div>
  </div>
  <a class="btn">View All</a>
</section>

<section class="block reviews">
  <h2 class="section-title">What our <span>people are saying</span></h2>
  <div class="review" style="left:120px;width:301px">
    <div class="mark"></div>
    <p style="padding:0 30px">Lorem Ipsum is simply dummy text of the printing andtypesetting industry. Lorem Ipsum has industry's standard,remaining essentially unchanged...</p>
    <svg class="wave" width="301" height="110" viewBox="0 0 301 110"><path d="M0 30 Q150 -10 301 30 L301 110 L0 110Z" fill="#f26522"/></svg>
    <div class="avatar" role="img" aria-label="Customer portrait"></div>
    <div class="who">Owen Marsh - Manager</div>
  </div>
  <div class="review" style="left:449px;width:631px">
    <div class="quote">&ldquo;</div>
    <p style="padding:0 40px;font-style:normal">Lorem ipsum dolor sit amet, consectetur adipiscing elit, sed do eiusmod tempor incididunt ut labore et dolore magna aliqua. Ut enim ad minim veniam, quis nostrud exercitation ullamco laboris nisi ut aliquip ex ea commodo consequat. Duis aute irure dolor in reprehenderit in voluptate velit esse cillum dolore eu fugiat ...</p>
    <svg class="wave" width="631" height="180" viewBox="0 0 631 180"><defs><linearGradient id="rv" x1="0" x2="1"><stop offset="0" stop-color="#f26522"/><stop offset=".55" stop-color="#6a3a6a"/><stop offset="1" stop-color="#1d2f66"/></linearGradient></defs><path d="M0 100 Q320 110 631 0 L631 180 L0 180Z" fill="url(#rv)"/></svg>
    <div class="avatar" role="img" aria-label="Customer portrait"></div>
    <div class="who">Clara Dunn - Manager</div>
  </div>
  <div class="dots" style="left:220px;width:100px"><i class="on"></i><i></i><i></i><i></i></div>
  <div class="dots" style="left:715px;width:100px"><i class="on"></i><i></i><i></i><i></i></div>
</section>

<section class="block team">
  <h2 class="section-title">Our <span>Team</span></h2>
  <span class="arrow prev"></span><span class="arrow next"></span>
  <div class="member" style="left:120px">
    <div class="photo" style="background:linear-gradient(160deg,#8a7a6a,#3a2e24)" role="img" aria-label="Team member at a desk"></div>
    <div class="num">01</div>
    <h4>Leo Hart</h4><div class="role">Managing Director</div>
    <p>Lorem Ipsum is simply dummy text of the printing andtypesetting industry.</p>
    <div class="more">Read More &rsaquo;</div>
  </div>
  <div class="member" style="left:452px">
    <div class="photo" style="background:linear-gradient(160deg,#d8d4d0,#5a5a62)" role="img" aria-label="Team member with headset at a computer"></div>
    <div class="num">02</div>
    <h4>Mark Ellis</h4><div class="role">Managing Director</div>
    <p>Lorem Ipsum is simply dummy text of the printing andtypesetting industry.</p>
    <div class="more">Read More &rsaquo;</div>
  </div>
  <div class="member" style="left:784px">
    <div class="photo" style="background:linear-gradient(160deg,#e8ece8,#8aa0b0)" role="img" aria-label="Team member in a bright office"></div>
    <div class="num">03</div>
    <h4>Ryan Cole</h4><div class="role">Managing Director</div>
    <p>Lorem Ipsum is simply dummy text of the printing andtypesetting industry.</p>
    <div class="more">Read More &rsaquo;</div>
  </div>
</section>

<footer class="block footer">
  <svg class="footer-bg" width="1200" height="498" viewBox="0 0 1200 498" preserveAspectRatio="none">
    <defs><radialGradient id="ft" cx=".55" cy=".8" r=".8"><stop offset="0" stop-color="#2a4488"/><stop offset="1" stop-color="#16254f"/></radialGradient></defs>
    <path d="M0 60 Q600 -40 1200 60 L1200 498 L0 498Z" fill="url(#ft)"/>
    <path d="M0 60 Q600 -40 1200 60" fill="none" stroke="#f26522" stroke-width="12"/>
  </svg>
  <div class="footer-cols">
    <div class="col"><h5>Quick Links</h5><div class="current">Home</div><div>About Us</div><div>Services</div><div>Team</div><div>Project</div><div>Contact Us</div></div>
    <div class="col"><h5>Contact Us</h5><div class="call">Call. <span>1-800-555-0142</span></div><div class="orange">&#9993; hello@lumenwell.example</div><div style="margin-top:14px">Address:</div><div>Lorem Ipsum is simply dummy<br>text of the printing andty<br>pesetting.</div></div>
    <div class="col"><h5>Business Hours</h5><div>Monday-Friday:9am to 5pm</div><div style="margin-top:10px">Saturday: 10am to 3pm</div><div style="margin-top:10px">Sunday: Closed</div></div>
    <div class="col"><h5>Follow US</h5><div class="socials"><span class="social"></span><span class="social"></span><span class="social"></span><span class="social"></span></div></div>
  </div>
  <div class="copyright">Copyright &copy; 2019. Lumenwell</div>
</footer>

</body>
</html>
```